Velmora Steam Cleaning website for demos

Velmora Steam Cleaning is a business that provides commercial cleaning services utilizing steam vapor, which offers the most effective and ecologically friendly method of cleaning today. We need a website to advertise our services, and needs to incorporate spaces to show video demonstrations on how the cleaning machine works.

Target Market(s)

The potential market for this business are hotels, motels, restaurants, hospitals, fast food facilities, nursing homes, day care centers, schools, country clubs, churches, office and apartment buildings, malls, movie theaters, super markets, airports, parks, and any other facility.

Industry/Entity Type

Business

Coding

Coded - Design and coding required

Number of Pages Required

3 page

Colors
add136
9bcb3c
34a6d7
3176b5
edf8f6

Requirements
Must have
• Areas for videos that serve as demonstrations of our services

```html
<!DOCTYPE html>
<html lang="en">
<head>
<meta charset="utf-8">
<title>Velmora Steam Cleaning</title>
<link href="https://fonts.googleapis.com/css2?family=Arimo:wght@400;700&family=Tinos&display=swap" rel="stylesheet">
<style>
  :root {
    --page-bg: #c5eaf7;
    --sky-deep: #1ec3f2;
    --sky-pale: #dff4fb;
    --nav-blue: #34a6d7;
    --brand-blue: #3176b5;
    --content-bg: #edf8f6;
    --text-dark: #444444;
    --nav-text: #1d3340;
    --frame-line: #ffffff;
  }
  * { margin: 0; padding: 0; box-sizing: border-box; }
  html, body {
    width: 1200px; height: 582px; overflow: hidden;
    background: var(--page-bg);
    font-family: "Arimo", Arial, sans-serif;
    color: var(--text-dark);
  }
  .site {
    position: absolute; left: 32px; top: 30px; width: 1137px;
    border: 1px solid var(--frame-line);
    border-radius: 11px; overflow: hidden;
  }
  .site-header {
    height: 93px;
    background: linear-gradient(to bottom, var(--sky-deep) 0%, var(--sky-pale) 100%);
    display: flex; align-items: center; padding-left: 22px;
  }
  .brand { display: flex; align-items: center; gap: 10px; }
  .brand-mark { width: 50px; height: 50px; }
  .brand-name {
    font-weight: 700; font-size: 22px; color: var(--brand-blue);
  }
  .main-nav {
    height: 33px; background: var(--nav-blue);
    display: flex; align-items: center; padding-left: 22px;
  }
  .main-nav a {
    font-family: "Tinos", "Times New Roman", serif;
    font-size: 13px; color: var(--nav-text); text-decoration: none;
    margin-right: 34px;
  }
  .content {
    height: 178px; background: var(--content-bg);
    padding: 24px 18px 0 18px;
  }
  .content h1 { font-size: 19px; font-weight: 700; margin-bottom: 11px; }
  .content h2 { font-size: 14px; font-weight: 700; margin-bottom: 10px; }
  .content p { font-size: 11px; line-height: 13px; margin-bottom: 11px; }
  .band { height: 13px; background: var(--nav-blue); }
  .site-footer {
    height: 55px;
    background: linear-gradient(to bottom, var(--sky-pale) 0%, var(--nav-blue) 100%);
    padding: 24px 0 0 22px; font-size: 10px; color: #222;
  }
</style>
</head>
<body>
  <div class="site">
    <header class="site-header">
      <div class="brand">
        <svg class="brand-mark" viewBox="0 0 50 50" aria-hidden="true">
          <circle cx="25" cy="25" r="24" fill="#9bcb3c"/>
        </svg>
        <span class="brand-name">Velmora Steam Cleaning</span>
      </div>
    </header>
    <nav class="main-nav">
      <a href="#">Home</a>
      <a href="#">Demonstrations</a>
      <a href="#">About us</a>
      <a href="#">Contact Us</a>
    </nav>
    <main class="content">
      <h1>Velmora Steam Cleaning</h1>
      <h2>Who are we?</h2>
      <p>Velmora Steam Cleaning is a business that provides commercial cleaning services utilizing steam vapor, which offers the most effective and ecologically friendly method of cleaning today.</p>
      <h2>Who do we provide services for?</h2>
      <p>The potential market for this business are hotels, motels, restaurants, hospitals, fast food facilities, nursing homes, day care centers, schools, country clubs, churches, office and apartment buildings, malls, movie theaters, super markets, airports, parks, and any other facility.</p>
    </main>
    <div class="band"></div>
    <footer class="site-footer">©</footer>
  </div>
</body>
</html>
```